Financial Advisor Resource Firm needs business card design

Need business card design for company in Omaha NE called Tallowbrook Alliance. We provide resources to financial advisors....workshop programs, retirement analysis, and insurance planning. I would like to see designs that use grays, greens, black, and white colors. The final design should communicate 'collaboration' and be simple yet attractive to financial planning clients. I will attached our logo and another picture of a puzzle piece coming together. I would like the incorporate the puzzle picture somehow, maybe on the back somehow, with color or just the gray scale....OR, the picture be the front of the card with 'Tallowbrook' definition on it (see upload) and then company logo, employee name, title, address on the back (see ppt uploaded). The following disclosure needs to be included somewhere- Advisory services offered through Hemstead Ledger, LLC.
Updates

I uploaded a svg and ai file of the logo

Target Market(s)

Financial planning clients and financial advisors....so pretty diverse age range of about 40-70.

Industry/Entity Type

Financial Planning

Contact Information for Business Card

Morris P. Quillfen, MBA
Founder/President
5327 E. Larkspur Avenue
Suite 418
Omaha, NE 68907
Phone- (402) 555-0147
Cell- (402) 555-0193
Fax- (402) 555-0126
email- morris@tallowbrookplan.example
web address- www.tallowbrookplan.example

Colors
1b1b1b
474747
d3d3d3
ffffff
9bcb3c
abd036

Requirements
Must have
• Must include logo provided, must be 2 sided, and must have disclosure...all of these items listed in project description

```html
<!DOCTYPE html>
<html lang="en">
<head>
<meta charset="UTF-8">
<title>Tallowbrook Alliance — Business Card</title>
<link href="https://fonts.googleapis.com/css2?family=Montserrat:wght@500;600&display=swap" rel="stylesheet">
<style>
  :root {
    --bg: #141414;
    --card: #1b1b1b;
    --card-edge: #262626;
    --gray-dark: #474747;
    --gray-light: #d3d3d3;
    --white: #ffffff;
    --green: #9bcb3c;
    --green-alt: #abd036;
  }
  * { margin: 0; padding: 0; box-sizing: border-box; }
  html, body {
    width: 1200px; height: 900px; overflow: hidden;
    background: var(--bg);
    font-family: "Montserrat", sans-serif;
  }
  .stage { position: relative; width: 1200px; height: 900px; }
  .card {
    position: absolute; left: 250px;
    width: 700px; height: 400px;
    background: linear-gradient(135deg, var(--card) 0%, #222 60%, var(--card) 100%);
    border: 1px solid var(--card-edge);
    box-shadow: 0 18px 40px rgba(0,0,0,.6);
  }
  .card--front { top: 40px; }
  .card--back { top: 460px; }

  .wordmark {
    display: flex; align-items: center; gap: 12px;
    font-weight: 600; letter-spacing: .04em; text-transform: uppercase;
  }
  .wordmark__dot { width: 16px; height: 16px; border-radius: 50%; flex: none; }

  .card--front .wordmark {
    position: absolute; inset: 0; justify-content: center;
    font-size: 36px; color: var(--gray-light);
  }
  .card--front .wordmark__dot { background: var(--gray-dark); }

  .card--back .wordmark {
    position: absolute; left: 40px; top: 176px; width: 290px;
    font-size: 20px; color: var(--white); line-height: 1.2;
  }
  .card--back .wordmark__dot { background: var(--green); }

  .divider {
    position: absolute; left: 360px; top: 60px;
    width: 2px; height: 280px; background: var(--green);
  }
  .contact {
    position: absolute; left: 388px; top: 62px; right: 24px;
    color: var(--white); font-weight: 500;
  }
  .contact__name { color: var(--green-alt); font-size: 24px; font-weight: 600; line-height: 1.1; }
  .contact__title { font-size: 14px; margin-top: 6px; }
  .contact__address { font-size: 14px; margin-top: 16px; line-height: 1.5; }
  .contact__list { list-style: none; margin-top: 16px; font-size: 14px; }
  .contact__list li { display: flex; align-items: center; gap: 10px; line-height: 1.75; }
  .contact__list svg { width: 13px; height: 13px; flex: none; stroke: var(--green); fill: none; stroke-width: 1.6; }
  .contact__hl { color: var(--green); }

  .disclosure {
    position: absolute; left: 0; right: 0; bottom: 18px;
    text-align: center; font-size: 10px; font-weight: 500;
    color: var(--gray-light); letter-spacing: .02em;
  }
</style>
</head>
<body>
<main class="stage">
  <section class="card card--front" aria-label="Card front">
    <div class="wordmark"><span class="wordmark__dot"></span>Tallowbrook Alliance</div>
  </section>

  <section class="card card--back" aria-label="Card back">
    <div class="wordmark"><span class="wordmark__dot"></span>Tallowbrook Alliance</div>
    <div class="divider"></div>
    <div class="contact">
      <h1 class="contact__name">Morris P. Quillfen, MBA</h1>
      <p class="contact__title">Founder/President</p>
      <p class="contact__address">5327 E. Larkspur Avenue<br>Suite 418 Omaha, NE 68907</p>
      <ul class="contact__list">
        <li><svg viewBox="0 0 16 16"><path d="M4 2l2 3-1.5 1.5c1 2 2.5 3.5 4.5 4.5L10.5 9.5l3 2-1 2.5C7 14 2 9 2 3z"/></svg><span>(402) 555-0147</span></li>
        <li><svg viewBox="0 0 16 16"><rect x="4.5" y="1.5" width="7" height="13" rx="1"/><path d="M7 12h2"/></svg><span>(402) 555-0193</span></li>
        <li><svg viewBox="0 0 16 16"><rect x="4" y="2" width="8" height="4"/><rect x="2" y="6" width="12" height="6"/><rect x="4" y="10" width="8" height="4"/></svg><span>(402) 555-0126</span></li>
        <li><svg viewBox="0 0 16 16"><rect x="1.5" y="3.5" width="13" height="9"/><path d="M1.5 3.5L8 9l6.5-5.5"/></svg><span>morris@tallowbrookplan.example</span></li>
        <li><svg viewBox="0 0 16 16"><circle cx="8" cy="8" r="6.5"/><path d="M1.5 8h13M8 1.5c-3 3.5-3 9.5 0 13M8 1.5c3 3.5 3 9.5 0 13"/></svg><span>www.<span class="contact__hl">tallowbrookplan</span>.example</span></li>
      </ul>
    </div>
    <p class="disclosure">Advisory services offered through Hemstead Ledger, LLC</p>
  </section>
</main>
</body>
</html>
```